Book cover for a racy book called: The Vixen's Manual For Strutting Boldly Into Midlife Romance

Cover for book called, "The Vixen's Manual For Strutting Boldly Into Midlife Romance" I'd like it to be edgy sexy and provocative. It's a silky leg with a killer stiletto getting out of a car door. It is a guy kissing the back of the neck of a woman. It is four women's hands toasting with martinis. Written by DawnMarie Fielding

Reason: New ideas for the cover! It's a silky leg with a killer stiletto getting out of a car door. It is a guy kissing the back of the neck of a woman. It is four women's hands toasting with martinis.

Target Market(s)

Women ages 35-60

Font styles to use
Serif
Sans Serif
Other font styles liked:
• Hattori Hanzo

Requirements
Must have
• It's a silky leg with a killer stiletto getting out of a car door. It is a guy kissing the back of the neck of a woman. It is four women's hands toasting with martinis. Edgy sexy vibe. I need a great artsy graphic using my face or entire body either with my picture or a characature of me. Lettering should reflect hot topics to grab attention. Title and author need to be prominant. Choose any of the pictures attached to sketch or characature.
Nice to have
• Get single women's opinions as to what they'd most likely pick up in a book store. The idea is to get the inspiration that any woman of any shape can look hot, sexy and confident without looking too young or slutty.
Should not have
• No picture of a cougar, would rather see confidence and sexy woman that any woman can become

```html
<!DOCTYPE html>
<html lang="en">
<head>
<meta charset="utf-8">
<title>The Vixen's Manual For Strutting Boldly Into Midlife Romance — DawnMarie Fielding</title>
<link rel="stylesheet" href="https://fonts.googleapis.com/css2?family=Russo+One&family=Oswald:wght@400&display=swap">
<style>
  :root {
    --ink-dark: #0d1012;
    --band-red-deep: #4a0f12;
    --band-red: #8e1a1d;
    --band-red-bright: #d42a26;
    --swirl-teal: #5fc9c3;
    --swirl-green: #3fbf55;
    --swirl-magenta: #a8335e;
    --swirl-navy: #2a3350;
    --author-blue: #5aa6ec;
    --author-blue-light: #b9dcff;
    --author-shade: #1d2f64;
    --author-white: #f1eefc;
    --author-white-shade: #4a3f7c;
    --subtitle-yellow: #f4ef1a;
    --figure-skin: #e2b08c;
    --figure-red: #a81c1a;
    --figure-blue: #2f78c6;
  }
  html, body {
    margin: 0;
    padding: 0;
    width: 848px;
    height: 1200px;
    overflow: hidden;
    background: #ffffff;
  }
  .cover {
    position: relative;
    width: 848px;
    height: 1200px;
    overflow: hidden;
    background: var(--swirl-navy);
  }
  .cover__top-band {
    position: absolute;
    left: 0; top: 0;
    width: 100%; height: 92px;
    background: linear-gradient(90deg, #141819, #1b2022 60%, #0e1112);
  }
  .cover__title-band {
    position: absolute;
    left: 0; top: 92px;
    width: 100%; height: 232px;
    background:
      repeating-linear-gradient(0deg, rgba(0,0,0,.08) 0 2px, transparent 2px 4px),
      repeating-linear-gradient(90deg, rgba(0,0,0,.06) 0 2px, transparent 2px 4px),
      linear-gradient(90deg, var(--band-red-deep), var(--band-red) 55%, var(--band-red-bright));
  }
  .cover__artwork {
    position: absolute;
    left: 0; top: 324px;
    width: 100%; height: 640px;
    background:
      radial-gradient(ellipse 30% 45% at 88% 55%, rgba(95,201,195,.85), transparent 70%),
      radial-gradient(ellipse 40% 30% at 45% 20%, rgba(63,191,85,.75), transparent 70%),
      radial-gradient(ellipse 35% 40% at 70% 75%, rgba(168,51,94,.8), transparent 70%),
      radial-gradient(ellipse 30% 50% at 8% 45%, rgba(90,120,50,.7), transparent 70%),
      radial-gradient(circle at 45% 55%, #3a4a6a, var(--swirl-navy) 45%, #141a24);
  }
  .cover__base-band {
    position: absolute;
    left: 0; top: 964px;
    width: 100%; height: 236px;
    background:
      repeating-linear-gradient(0deg, rgba(0,0,0,.08) 0 2px, transparent 2px 4px),
      repeating-linear-gradient(90deg, rgba(0,0,0,.06) 0 2px, transparent 2px 4px),
      linear-gradient(90deg, var(--band-red-deep), var(--band-red) 55%, var(--band-red-bright));
  }
  .cover__figure {
    position: absolute;
    left: 420px; top: 150px;
    width: 330px; height: 980px;
    border-radius: 140px 140px 60px 60px;
    background: linear-gradient(180deg,
      rgba(226,176,140,.85) 0%,
      rgba(168,28,26,.85) 22%,
      rgba(47,120,198,.85) 42%,
      rgba(226,176,140,.85) 58%,
      rgba(226,176,140,.6) 92%,
      rgba(47,120,198,.7) 100%);
  }
  .cover__author {
    position: absolute;
    left: 0; top: 72px;
    width: 100%;
    margin: 0;
    font-family: "Russo One", sans-serif;
    font-weight: 400;
    line-height: 1;
    text-transform: uppercase;
  }
  .cover__author-first {
    display: block;
    margin-left: 64px;
    font-size: 96px;
    color: var(--author-blue);
    background: linear-gradient(180deg, var(--author-blue-light), var(--author-blue) 60%, #2c6fc0);
    -webkit-background-clip: text;
    background-clip: text;
    -webkit-text-fill-color: transparent;
    filter: drop-shadow(4px 5px 0 var(--author-shade));
  }
  .cover__author-last {
    display: block;
    margin-top: 62px;
    margin-left: 150px;
    font-size: 96px;
    color: var(--author-white);
    text-shadow: 4px 5px 0 var(--author-white-shade);
  }
  .cover__subtitle {
    position: absolute;
    left: 0; top: 895px;
    width: 100%;
    margin: 0;
    font-family: "Oswald", sans-serif;
    font-weight: 400;
    font-size: 52px;
    line-height: 82px;
    color: var(--subtitle-yellow);
    text-transform: uppercase;
    text-align: center;
    text-shadow: 2px 2px 3px rgba(0,0,0,.45);
  }
  .cover__subtitle span { display: block; }
  .cover__subtitle .line-1 { margin-left: 60px; }
</style>
</head>
<body>
  <main class="cover">
    <div class="cover__top-band"></div>
    <div class="cover__title-band"></div>
    <div class="cover__artwork" role="img" aria-label="Abstract swirl of teal, green and magenta light"></div>
    <div class="cover__base-band"></div>
    <div class="cover__figure" role="img" aria-label="Caricature of the author standing confidently, hands on hips, in a red top, blue shorts and blue heels"></div>
    <h2 class="cover__author">
      <span class="cover__author-first">DawnMarie</span>
      <span class="cover__author-last">Fielding</span>
    </h2>
    <h1 class="cover__subtitle">
      <span class="line-1">The Vixen's Manual</span>
      <span>For Strutting Boldly</span>
      <span>Into Midlife Romance</span>
    </h1>
  </main>
</body>
</html>
```